BW Business Card

Used Car Sales
We are trying to recreate the image of our license plate on business cards,
it is a red background with a white oval that is open on the ends
I attempted to upload the image but it was a dismal failure when the products arrived
the lettering was too small and the edges were white
I think maybe the red needs some texture in it, still red but something that doesn't look so flat
and maybe a beveled edge around the white (not sure)

Target Market(s)

Adults 25-65 that drive

Industry/Entity Type

Business

Contact Information for Business Card

Rachel Thornbury, Sales Manager, BRIGHT WAY AUTO LOT, INC., 746 Ferris Lane, Dunmore, KY 42371,
270 555-0172 (office), 270 555-0849 (fax) - We Finance everyone with approved credit
BrightWayAutoLot.Com

On Back: Financing Available - We Finance everyone with approved credit
Easy Payments: Monthly, Semi-Monthly or Weekly
Ask about our Layaway plan
Open Mon-Sat
8:30 AM - 5 PM

Requirements
Must have
• We want to match the license plate (minus holes for screws)

```html
<!DOCTYPE html>
<html lang="en">
<head>
<meta charset="utf-8">
<title>Bright Way Auto Lot – Business Card</title>
<link rel="stylesheet" href="https://fonts.googleapis.com/css2?family=Tinos:wght@400;700&display=swap">
<style>
  :root {
    --backdrop: #e6e7e9;
    --plate-red: #d42a26;
    --plate-red-deep: #b81d1b;
    --oval-white: #f7f7f5;
    --oval-edge: #3a3a3a;
    --ink: #111111;
    --highlight: #ecdf2a;
  }
  * { margin: 0; padding: 0; box-sizing: border-box; }
  html, body {
    width: 1200px; height: 720px; overflow: hidden;
    background: var(--backdrop);
  }
  .canvas { position: relative; width: 1200px; height: 720px; }
  .card {
    position: absolute; top: 242px;
    width: 420px; height: 238px;
    box-shadow: 0 10px 24px rgba(0,0,0,.25);
    font-family: "Tinos", "Times New Roman", serif;
    color: var(--ink);
  }
  .card--front { left: 147px; }
  .card--back { left: 633px; }
  .card__plate { position: absolute; inset: 0; width: 100%; height: 100%; display: block; }
  .line {
    position: absolute; left: 0; right: 0;
    text-align: center; white-space: nowrap;
    font-size: 12.5px; line-height: 16px;
  }
  .line--bold { font-weight: 700; }
  .name { top: 50px; font-size: 14px; font-weight: 700; letter-spacing: .3px; }
  .title { top: 67px; }
  .company { top: 98px; }
  .company span {
    background: var(--highlight);
    font-size: 16px; font-weight: 700; padding: 1px 2px;
  }
  .address { top: 115px; }
  .office { top: 131px; }
  .fax { top: 146px; }
  .web { top: 161px; }
  .finance { top: 176px; }
  .back-1 { top: 86px; }
  .back-2 { top: 105px; }
  .back-3 { top: 124px; }
  .back-4 { top: 162px; }
</style>
</head>
<body>
<div class="canvas">

  <section class="card card--front">
    <svg class="card__plate" viewBox="0 0 420 238" aria-hidden="true">
      <defs>
        <radialGradient id="redFront" cx="50%" cy="50%" r="70%">
          <stop offset="0" stop-color="var(--plate-red)"/>
          <stop offset="1" stop-color="var(--plate-red-deep)"/>
        </radialGradient>
      </defs>
      <rect width="420" height="238" fill="url(#redFront)"/>
      <ellipse cx="210" cy="119" rx="227" ry="101" fill="var(--oval-white)" stroke="var(--oval-edge)" stroke-width="1.2"/>
    </svg>
    <p class="line name">RACHEL THORNBURY</p>
    <p class="line title">Sales Manager</p>
    <p class="line company"><span>BRIGHT WAY AUTO LOT, INC</span></p>
    <p class="line address">746 Ferris Lane, Dunmore, KY 42371</p>
    <p class="line office">Office &nbsp;&nbsp;&nbsp;: &nbsp;&nbsp;270 555-0172</p>
    <p class="line fax">Fax &nbsp;: &nbsp;&nbsp;270 555-0849</p>
    <p class="line web">BrightWayAutoLot.Com</p>
    <p class="line line--bold finance">We Finance everyone with approved credit!</p>
  </section>

  <section class="card card--back">
    <svg class="card__plate" viewBox="0 0 420 238" aria-hidden="true">
      <defs>
        <radialGradient id="redBack" cx="50%" cy="50%" r="70%">
          <stop offset="0" stop-color="var(--plate-red)"/>
          <stop offset="1" stop-color="var(--plate-red-deep)"/>
        </radialGradient>
      </defs>
      <rect width="420" height="238" fill="url(#redBack)"/>
      <ellipse cx="210" cy="119" rx="227" ry="101" fill="var(--oval-white)" stroke="var(--oval-edge)" stroke-width="1.2"/>
    </svg>
    <p class="line line--bold back-1">Financing Available - We Finance everyone with approved credit!</p>
    <p class="line back-2">Easy Payments: Monthly, Semi-Monthly or Weekly</p>
    <p class="line line--bold back-3">Ask about our Lay-away plan</p>
    <p class="line line--bold back-4">Open Mon-Sat 8:30 AM - 5 PM</p>
  </section>

</div>
</body>
</html>
```